Email Newsletter Banner

I require 2 new email newsletter and web banners to be made up.
I require the brand names to be included on the banner which are " Wire Dispatcher" and "PC Flashz". I would also like some sort of imagery and also a "sign up here" button. Please see below examples:
https://dataskyreports.lornexhub.com/
https://datawisdomsky.lornexhub.com/
https://datastoryvault.lornexhub.com/

```html
<!DOCTYPE html>
<html lang="en">
<head>
<meta charset="utf-8">
<title>Newsletter Designs – Wire Dispatcher &amp; PC Flashz</title>
<link href="https://fonts.googleapis.com/css2?family=Figtree:wght@400;500;600;700;800&display=swap" rel="stylesheet">
<style>
  :root {
    --navy: #172c4f;
    --teal: #00a0a4;
    --ice: #eaf1fb;
    --white: #ffffff;
    --ink: #2a2a2a;
    --body: #555a60;
    --backdrop: #c7c7c7;
  }
  * { box-sizing: border-box; margin: 0; padding: 0; }
  html, body { width: 1200px; height: 1152px; overflow: hidden; }
  body {
    background: var(--backdrop);
    font-family: "Figtree", Arial, sans-serif;
    position: relative;
  }
  .newsletter, .banner {
    position: absolute;
    width: 337px;
    background: var(--white);
    box-shadow: 0 6px 22px rgba(0,0,0,.22);
    overflow: hidden;
  }
  .newsletter { top: 72px; height: 1008px; }
  .newsletter--dispatcher { left: 70px; }
  .newsletter--flashz { left: 435px; }
  .abs { position: absolute; }

  .hero { position: absolute; left: 0; top: 0; width: 337px; height: 185px; }
  .hero--walk {
    background: linear-gradient(180deg, #1d335a 0%, #34507a 28%, #b9bec4 55%, #d9d6cf 80%, #c4b59b 100%);
  }
  .hero--tablet {
    background: linear-gradient(120deg, #1a2a44 0%, #2f4566 35%, #8b7f78 60%, #4a4e58 80%, #2b2f38 100%);
  }
  .masthead { color: var(--white); font-weight: 700; letter-spacing: .2px; }
  .btn-signup {
    position: absolute;
    color: var(--white);
    font-size: 8px;
    font-weight: 700;
    display: flex; align-items: center; justify-content: center;
  }

  /* Wire Dispatcher */
  .newsletter--dispatcher .masthead { left: 26px; top: 12px; font-size: 21px; }
  .newsletter--dispatcher .btn-signup {
    left: 237px; top: 12px; width: 73px; height: 23px;
    background: var(--teal); border-radius: 12px 0 0 12px;
  }
  .welcome-title {
    left: 26px; top: 206px; font-size: 29px; line-height: 36px; font-weight: 800; color: var(--teal);
  }
  .body-copy {
    font-size: 7.6px; line-height: 15.2px; color: var(--body); text-align: justify;
  }
  .newsletter--dispatcher .body-copy { left: 26px; top: 251px; width: 280px; }
  .highlights { left: 26px; top: 569px; list-style: none; }
  .highlights li {
    font-size: 12.5px; font-weight: 500; color: var(--ink);
    line-height: 19.6px; padding-left: 24px; position: relative; white-space: nowrap;
  }
  .highlights li::before {
    content: ""; position: absolute; left: 3px; top: 8px;
    width: 6px; height: 6px; border-radius: 50%; background: var(--teal);
  }
  .signup-board { left: 0; top: 734px; width: 337px; height: 141px; background: #d8d8d8; }
  .signup-board__person { position: absolute; top: 0; height: 141px; }
  .signup-board__person--left { left: 0; width: 64px; background: linear-gradient(90deg, #9a9a9a, #c9c4bf); }
  .signup-board__person--right { right: 0; width: 78px; background: linear-gradient(90deg, #bdb8b3, #5e6268); }
  .signup-board__card {
    position: absolute; left: 64px; top: 0; width: 195px; height: 141px;
    background: #f4f4f4; text-align: center; padding-top: 33px;
    font-weight: 800; font-size: 33px; line-height: 37px;
  }
  .signup-board__card .line1 { color: var(--navy); }
  .signup-board__card .line2 { color: var(--teal); }

  .footer { left: 0; width: 337px; text-align: center; }
  .newsletter--dispatcher .footer { top: 875px; height: 133px; background: var(--navy); color: var(--white); }
  .newsletter--flashz .footer { top: 882px; height: 126px; background: var(--white); color: var(--ink); }
  .social { position: absolute; left: 0; width: 337px; display: flex; justify-content: center; gap: 7px; }
  .social span { width: 29px; height: 29px; border-radius: 50%; background: var(--teal); display: block; }
  .footer-links { position: absolute; left: 0; width: 337px; font-size: 9.5px; line-height: 12px; font-weight: 700; letter-spacing: .1px; }
  .footer-links i { font-style: normal; margin: 0 9px; font-weight: 500; }
  .copyright { position: absolute; left: 0; width: 337px; font-size: 8px; line-height: 10px; }
  .newsletter--dispatcher .social { top: 28px; }
  .newsletter--dispatcher .footer-links { top: 74px; }
  .newsletter--dispatcher .copyright { top: 100px; }
  .newsletter--flashz .social { top: 21px; }
  .newsletter--flashz .footer-links { top: 67px; }
  .newsletter--flashz .copyright { top: 93px; color: #333; }

  /* PC Flashz */
  .newsletter--flashz .masthead { left: 26px; top: 18px; font-size: 22px; }
  .newsletter--flashz .btn-signup {
    left: 264px; top: 125px; width: 75px; height: 27px;
    background: var(--navy); border: 2px solid var(--teal); border-right: 0;
    border-radius: 14px 0 0 14px;
  }
  .welcome-band {
    left: 26px; top: 185px; width: 285px; height: 53px; background: var(--teal);
    color: var(--white); font-size: 22px; font-weight: 800;
    display: flex; align-items: center; justify-content: center;
  }
  .columns .body-copy { position: absolute; width: 132px; font-size: 6.9px; line-height: 12.3px; }
  .columns .col-a { left: 26px; top: 259px; }
  .columns .col-b { left: 178px; top: 256px; }
  .features { left: 0; top: 532px; width: 337px; height: 291px; background: var(--ice); }
  .features__title {
    position: absolute; left: 0; width: 337px; top: 35px; text-align: center;
    font-size: 22px; line-height: 26px; font-weight: 700; color: var(--ink);
  }
  .feature { position: absolute; width: 128px; }
  .feature--a { left: 26px; top: 89px; }
  .feature--b { left: 182px; top: 89px; }
  .feature--c { left: 26px; top: 181px; }
  .feature--d { left: 182px; top: 181px; }
  .feature__num {
    width: 30px; height: 30px; border-radius: 50%; color: var(--white);
    font-size: 11px; font-weight: 700; display: flex; align-items: center; justify-content: center;
  }
  .feature__num--teal { background: var(--teal); }
  .feature__num--navy { background: var(--navy); }
  .feature p { margin-top: 7px; font-size: 7.8px; line-height: 13px; font-weight: 600; color: var(--ink); text-align: justify; }
  .signup-band {
    left: 0; top: 823px; width: 337px; height: 59px; background: var(--navy);
    color: var(--white); font-size: 25px; font-weight: 800;
    display: flex; align-items: center; justify-content: center;
  }

  /* web banners */
  .banner { left: 793px; height: 186px; }
  .banner--walk { top: 72px; }
  .banner--tablet { top: 274px; }
  .banner .hero { height: 186px; }
</style>
</head>
<body>

<section class="newsletter newsletter--dispatcher">
  <div class="hero hero--walk" role="img" aria-label="Photo of two business colleagues walking past a columned building, one holding a laptop"></div>
  <h1 class="abs masthead">Wire Dispatcher</h1>
  <div class="btn-signup">SIGN UP HERE</div>

  <h2 class="abs welcome-title">Welcome</h2>
  <p class="abs body-copy">Lorem ipsum dolor sit amet, consectetur adipiscing elit, sed do eiusmod tempor incididunt ut labore et dolore magna aliqua. Quis ipsum suspendisse ultrices g commodo viverra maecenas accumsan lacus vel facilisis. Lorem ipsum dolor sit amet, consectetur adipiscing elit, sed do eiusmod tempor incididunt ut labore et dolore msum suspendisse ultricemodo viverra maececcumsan lacus vel facilisis. Lorem ipsum dolor sit amet, consectetur adipiscing elit, sed do eiusmod tempor incididunt ut labore et dolore magna aliqua. Quis ipsum suspendisse ultrices g commodo viverra maecenas accumsan lacus vel facilisis. Lorem ipsum dolor sit amet, consectetur adipiscing elit, sed do eiusmod tempor incididunt ut labore et dolore msum suspendisse ultricemodo viverra maececcumsan lacus vel facilisis. Lorem ipsum dolor sit amet, consectetur adipiscing elit, sed do eiusmod tempor incididunt ut labore et dolore magna aliqua. Quis ipsum suspendisse ultrices g commodo viverra maecenas accumsan lacus vel facilisis. Lorem ipsum dolor sit amet, consectetur adipiscing elit, sed do eiusmod tempor incididunt ut labore et dolore msum suspendisse ultricemodo viverra maececcumsan lacus vel facilisis. Lorem ipsum dolor sit amet, consectetur adipiscing elit, sed do eiusmod tempor incididunt ut labore et dolore magna aliqua. Quis ipsum suspendisse ultrices g commodo viverra maecenas accumsan lacus vel facilisis. Lorem ipsum dolor sit amet, consectetur adipiscing elit, sed do eiusmod tempor incididunt ut labore et dolore msum suspendisse ultricemodo viverra maececcumsan lacus vel facilisis.</p>

  <ul class="abs highlights">
    <li>Lorem ipsum dolor sionsectetur adipiscin</li>
    <li>Excepteur sint occaecat cupidatat non proi</li>
    <li>Ut enim ad minima veniamquis</li>
    <li>Nemo enim ipsam voluptatem qui</li>
    <li>Quis autem vel eum iure reprehende</li>
    <li>Vel illum qui dolorem eum fugiat quo</li>
    <li>Minim veniamquis nostrud exercitatio</li>
  </ul>

  <div class="abs signup-board">
    <div class="signup-board__person signup-board__person--left" role="img" aria-label="Photo of a smiling woman pointing at the sign"></div>
    <div class="signup-board__card"><div class="line1">SIGN UP</div><div class="line2">HERE</div></div>
    <div class="signup-board__person signup-board__person--right" role="img" aria-label="Photo of a smiling man in a suit pointing at the sign"></div>
  </div>

  <footer class="abs footer">
    <div class="social" aria-label="Social links"><span></span><span></span><span></span></div>
    <div class="footer-links">PRIVACY POLICY<i>/</i>TERMS OF USE<i>/</i>SITEMAP<i>/</i>FAQ</div>
    <div class="copyright">© 2022 Wire Dispatcher. All rights reserved.Privacy</div>
  </footer>
</section>

<section class="newsletter newsletter--flashz">
  <div class="hero hero--tablet" role="img" aria-label="Photo of two young professionals looking at a tablet together"></div>
  <h1 class="abs masthead">PC Flashz</h1>
  <div class="btn-signup">SIGN UP HERE</div>

  <h2 class="abs welcome-band">WELCOME TO PC FLASHZ</h2>

  <div class="columns">
    <p class="body-copy col-a">Lorem ipsum dolor sit amet, consectetur adipiscing elit, sed do eiusmod tempor incididunt ut labore et dolore magna aliqua. Quis ipsum suspendisse ultrices g commodo viverra maecenas accumsan lacus vel facilisis. Lorem ipsum dolor sit amet, consectetur adipiscing elit, sed do eiusmod tempor incididunt ut labore et dolore msum suspendisse ultricemodo viverra maececcumsan lacus vel facilisis. Lorem ipsum dolor sit amet, consectetur adipiscing elit, sed do eiusmod tempor incididunt ut labore et dolore magna aliqua. Quis ipsum suspendisse ultrices g commodo viverra maecenas accumsan lacus vel facilisis. Lorem ipsum dolor sit amet, consectetur adipiscing elit, sed do eiusmod tempor incididunt ut labore et dolore msum suspendisse ultricemodo viverra maececcumsan lacus vel facilisis.</p>
    <p class="body-copy col-b">Lorem ipsum dolor sit amet, consectetur adipiscing elit, sed do eiusmod tempor incididunt ut labore et dolore magna aliqua. Quis ipsum suspendisse ultrices g commodo viverra maecenas accumsan lacus vel facilisis. Lorem ipsum dolor sit amet, consectetur adipiscing elit, sed do eiusmod tempor incididunt ut labore et dolore msum suspendisse ultricemodo viverra maececcumsan lacus vel facilisis. Lorem ipsum dolor sit amet, consectetur adipiscing elit, sed do eiusmod tempor incididunt ut labore et dolore magna aliqua. Quis ipsum suspendisse ultrices g commodo viverra maecenas accumsan lacus vel facilisis. Lorem ipsum dolor sit amet, consectetur adipiscing elit, sed do eiusmod tempor incididunt ut labore et dolore msum suspendisse ultricemodo viverra maececcumsan lacus vel facilisis.</p>
  </div>

  <div class="abs features">
    <h3 class="features__title">KEY FEATURES</h3>
    <div class="feature feature--a">
      <div class="feature__num feature__num--teal">01</div>
      <p>Lorem ipsum dolor sit aonsectetur adipiscing elit, sed do eiusmod tempor incididunt ut labore</p>
    </div>
    <div class="feature feature--b">
      <div class="feature__num feature__num--navy">02</div>
      <p>Lorem ipsum dolor sit aonsectetur adipiscing elit, sed do eiusmod tempor incididunt ut labore</p>
    </div>
    <div class="feature feature--c">
      <div class="feature__num feature__num--navy">03</div>
      <p>Lorem ipsum dolor sit aonsectetur adipiscing elit, sed do eiusmod tempor incididunt ut labore</p>
    </div>
    <div class="feature feature--d">
      <div class="feature__num feature__num--teal">04</div>
      <p>Lorem ipsum dolor sit aonsectetur adipiscing elit, sed do eiusmod tempor incididunt ut labore</p>
    </div>
  </div>

  <div class="abs signup-band">SIGN UP HERE</div>

  <footer class="abs footer">
    <div class="social" aria-label="Social links"><span></span><span></span><span></span></div>
    <div class="footer-links">PRIVACY POLICY<i>/</i>TERMS OF USE<i>/</i>SITEMAP<i>/</i>FAQ</div>
    <div class="copyright">© 2022 PC Flashz. All rights reserved.Privacy</div>
  </footer>
</section>

<div class="banner banner--walk">
  <div class="hero hero--walk" role="img" aria-label="Web banner photo of two business colleagues walking past a columned building"></div>
</div>
<div class="banner banner--tablet">
  <div class="hero hero--tablet" role="img" aria-label="Web banner photo of two young professionals looking at a tablet"></div>
</div>

</body>
</html>
```